Velmora web stylesheet and logo

We are developing a new site for Velmora and would like someone to provide a new logo and a web page style guide.
This company connects carriers with with customers that need specialty moves: store fixtures, displays, exhibits, technology, manufacturing equipment, etc.
We want to convey quality customer service, quality transportation, and the use of current technology in our business. We do not want to look like a trucking company.
Logo needs a total remake!!!

Target Market(s)

Technology, Retail, Manufacturing, Hospitalty...

Industry/Entity Type

It Company

Logo Text

we will provide some thing soon

Number of Pages Required

1 page

Font styles to use
Serif
Sans Serif

Requirements
Must have
• Warm colors, professional looking.
Nice to have
• If you have pics to include we'll consider
Should not have
• We must no look like a trucking company.

```html
<!DOCTYPE html>
<html lang="en">
<head>
<meta charset="utf-8">
<title>Velmora</title>
<link href="https://fonts.googleapis.com/css2?family=Alfa+Slab+One&family=Lato:wght@300;400;700;900&display=swap" rel="stylesheet">
<style>
:root{
  --orange:#f26a10;
  --orange-dark:#d85a08;
  --ink:#1f1f1f;
  --bar:#2d2d2d;
  --footer:#2a2a2a;
  --light:#ececec;
  --text:#333;
  --muted:#ccc;
  --box1:#444;
  --box2:#545454;
  --box3:#5f5f5f;
  --plus:#8a5a3c;
}
*{margin:0;padding:0;box-sizing:border-box}
html,body{width:1200px;height:2941px;overflow:hidden}
body{font-family:"Lato",sans-serif;color:var(--text);background:#fff;position:relative}
section,header,footer,div,a,span,p,h1,h2,h3,li{position:relative}
.abs{position:absolute}
.slab{font-family:"Alfa Slab One",serif;font-weight:400}
.btn{position:absolute;display:flex;align-items:center;justify-content:center;background:var(--orange);color:#fff;font-weight:700;font-size:12px;text-decoration:none}

/* top bar */
.top-bar{height:39px;background:var(--bar)}
.social-top{position:absolute;right:167px;top:12px;display:flex;gap:14px}
.social-top span{width:12px;height:12px;background:var(--orange);border-radius:2px}

/* header */
.site-header{height:108px;background:#fff}
.brand{position:absolute;left:161px;top:28px;display:flex;align-items:center;gap:10px;font-family:"Lato",sans-serif;font-weight:900;font-size:30px;color:var(--ink);letter-spacing:1px}
.brand .mark{width:22px;height:22px;background:var(--orange)}
.contact-inline{position:absolute;top:22px;display:flex;align-items:center;gap:10px;font-size:14px;color:#222}
.main-nav{position:absolute;left:421px;top:63px;right:0;height:45px;background:var(--orange);clip-path:polygon(0 0,100% 0,100% 100%,28px 100%)}
.main-nav a{position:absolute;top:14px;color:#fff;font-size:12px;text-decoration:none;text-transform:uppercase}
.main-nav a.active{font-weight:700}

/* hero */
.hero{height:457px;background:linear-gradient(180deg,#5b6875 0%,#8a96a0 35%,#6f7a72 70%,#3e4a3a 100%);text-align:center;color:#fff}
.hero-photo{position:absolute;inset:0;background:radial-gradient(ellipse at 55% 40%,rgba(200,205,210,.55),rgba(0,0,0,0) 60%)}
.hero h1{position:absolute;top:190px;left:0;right:0;font-size:44px;text-shadow:0 2px 4px rgba(0,0,0,.5)}
.hero p{position:absolute;top:252px;left:0;right:0;font-size:17px;font-weight:700;text-shadow:0 1px 3px rgba(0,0,0,.6)}
.hero .btn{left:506px;top:310px;width:188px;height:51px;font-size:24px;font-weight:400}

/* section titles */
.section-title{position:absolute;left:0;right:0;text-align:center;font-size:24px;letter-spacing:1px;color:var(--ink)}
.section-title em{font-style:normal;color:var(--orange)}
.divider{position:absolute;left:540px;width:120px;height:14px}
.on-dark .section-title{color:#fff}

/* about */
.about{height:321px;background:var(--light)}
.about p{position:absolute;left:186px;width:843px;top:153px;text-align:center;font-size:12px;line-height:19px;color:#333}

/* services */
.services{height:693px;background:linear-gradient(180deg,#3a3f44 0%,#2a2c2e 45%,#111 100%)}
.services .lead{position:absolute;top:152px;left:0;right:0;text-align:center;color:#fff;font-size:16px;font-weight:700}
.service-card{position:absolute;top:218px;width:276px;text-align:center}
.service-card .photo{height:274px;border:3px solid #5a3a25}
.service-card h3{margin-top:28px;color:var(--orange);font-size:16px;font-weight:700;text-transform:uppercase}
.service-card p{margin-top:12px;color:#eee;font-size:12px;line-height:19px}
.service-card .btn{left:84px;top:386px;width:108px;height:28px}
.arrow{position:absolute;top:340px}

/* why */
.why{height:431px;background:var(--light)}
.why-box{position:absolute;top:148px;width:293px;height:222px;color:#eee;text-align:center;box-shadow:0 10px 12px -6px rgba(0,0,0,.45)}
.why-box svg{position:absolute;left:50%;transform:translateX(-50%);top:28px}
.why-box h3{position:absolute;top:112px;left:0;right:0;font-size:14px;font-weight:700;color:var(--orange)}
.why-box p{position:absolute;top:136px;left:40px;right:40px;font-size:12px;line-height:19px}
.why-box .plus{position:absolute;right:0;bottom:0;width:26px;height:26px;background:var(--plus);color:#fff;font-weight:700;font-size:20px;display:flex;align-items:center;justify-content:center}

/* blog */
.blog{height:549px;background:linear-gradient(180deg,#3a3c3e,#1c1d1e 60%,#2a2a2a)}
.post{position:absolute;top:176px;width:261px;color:#fff}
.post .photo{height:151px;border:2px solid #ddd}
.post .date{position:absolute;left:106px;top:128px;width:52px;height:42px;background:var(--orange);text-align:center;font-family:"Alfa Slab One",serif;font-size:11px;line-height:15px;padding-top:5px}
.post .date b{display:block;font-size:14px;font-weight:400}
.post .meta{display:flex;justify-content:space-between;padding:8px 10px 0;font-size:10px;color:#ddd}
.post h3{margin-top:12px;font-size:15px;font-weight:700}
.post p{margin-top:8px;font-size:12px;line-height:19px;color:#ccc}
.post .btn{left:80px;top:274px;width:104px;height:30px}

/* newsletter */
.newsletter{height:73px;background:#eee}
.newsletter .title{position:absolute;left:216px;top:16px;font-size:28px;font-weight:300;color:var(--orange)}
.newsletter input{position:absolute;left:506px;top:15px;width:423px;height:40px;border:1px solid #ccc;background:#fff;padding-left:14px;font:13px "Lato",sans-serif;color:#777}
.newsletter .btn{left:955px;top:22px;width:82px;height:28px;font-size:15px}

/* footer */
.site-footer{height:231px;background:var(--footer);color:#ddd}
.site-footer h4{position:absolute;top:38px;color:var(--orange);font-size:14px;font-weight:700;padding-bottom:6px;border-bottom:1px solid #555;width:150px}
.links{position:absolute;left:163px;top:74px;list-style:none;font-size:12px;line-height:19.6px}
.links li::before{content:"›";margin-right:8px;color:#fff}
.contact-detail{position:absolute;left:369px;top:74px;width:200px;font-size:12px;line-height:17px}
.contact-detail .row{display:flex;align-items:center;gap:10px;margin-top:10px}
.inquiry{position:absolute;left:598px;top:74px}
.inquiry div{width:180px;height:20px;background:#fff;color:#666;font-size:10px;padding:4px 6px;margin-bottom:10px}
.inquiry .btn{position:relative;width:66px;height:20px;font-size:11px}
.footer-brand{position:absolute;left:813px;top:62px;display:flex;align-items:center;gap:10px;font-weight:900;font-size:28px;color:#fff}
.footer-brand .mark{width:22px;height:22px;background:#bbb}
.social-foot{position:absolute;left:853px;top:140px;display:flex;gap:10px}
.social-foot span{width:28px;height:28px;border-radius:50%;background:var(--orange)}
.copyright{height:39px;background:#1a1a1a;color:#ccc;font-size:11px;text-align:center;line-height:39px}
.copyright em{font-style:normal;color:var(--orange)}
</style>
</head>
<body>

<div class="top-bar">
  <div class="social-top"><span></span><span></span><span></span><span></span><span></span></div>
</div>

<header class="site-header">
  <div class="brand"><span class="mark"></span>VELMORA</div>
  <div class="contact-inline" style="left:703px">
    <svg width="14" height="11" viewBox="0 0 14 11"><rect width="14" height="11" rx="1" fill="#f26a10"/><path d="M0 1l7 5 7-5" stroke="#fff" stroke-width="1.3" fill="none"/></svg>
    info@velmora-mail.com
  </div>
  <div class="contact-inline" style="left:928px">
    <svg width="13" height="13" viewBox="0 0 24 24"><path fill="#f26a10" d="M6.6 10.8a15 15 0 006.6 6.6l2.2-2.2c.3-.3.7-.4 1-.2 1.1.4 2.3.6 3.6.6.6 0 1 .4 1 1V20c0 .6-.4 1-1 1A17 17 0 013 4c0-.6.4-1 1-1h3.5c.6 0 1 .4 1 1 0 1.3.2 2.5.6 3.6.1.3 0 .7-.2 1z"/></svg>
    555 014 2870
  </div>
  <nav class="main-nav">
    <a class="active" style="left:40px">Home</a>
    <a style="left:159px">About Us</a>
    <a style="left:267px">Careers</a>
    <a style="left:373px">Services</a>
    <a style="left:471px">Blog</a>
    <a style="left:539px">Contact Us</a>
  </nav>
</header>

<section class="hero">
  <div class="hero-photo" role="img" aria-label="Heavy-haul truck carrying a large oversize cylindrical load on a highway"></div>
  <h1 class="slab">We Provide</h1>
  <p>Quality Transportation, And The Use Of Current Technology In Our Business.</p>
  <a class="btn">CALL US NOW</a>
</section>

<section class="about">
  <h2 class="section-title slab" style="top:78px">ABOUT <em>VELMORA</em></h2>
  <svg class="divider" style="top:122px" viewBox="0 0 120 14"><line x1="0" y1="7" x2="50" y2="7" stroke="#aaa"/><line x1="70" y1="7" x2="120" y2="7" stroke="#aaa"/><rect x="55" y="2" width="10" height="10" rx="2" fill="none" stroke="#888" stroke-width="1.5"/></svg>
  <p>Lorem ipsum dolor sit amet, consectetuer adipiscing elit, sed diam nonummy nibh euismod tincidunt ut laoreet dolore magna aliquam erat volutpat. Ut wisi enim ad minim veniam, quis nostrud exerci tation ullamcorper suscipit lobortis nisl ut aliquip ex ea commodo consequat. Duis autem vel eum iriure dolor in hendrerit in vulputate velit esse molestie consequat, vel illum dolore eu feugiat nulla facilisis at vero eros.</p>
  <a class="btn" style="left:547px;top:237px;width:106px;height:31px">Read More »</a>
</section>

<section class="services on-dark">
  <h2 class="section-title slab" style="top:84px">WHAT WE DO?</h2>
  <svg class="divider" style="top:119px" viewBox="0 0 120 14"><line x1="0" y1="7" x2="50" y2="7" stroke="#777"/><line x1="70" y1="7" x2="120" y2="7" stroke="#777"/><rect x="55" y="2" width="10" height="10" rx="2" fill="none" stroke="#bbb" stroke-width="1.5"/></svg>
  <p class="lead">Our Firm Connects Trucks With Customers That Need Specialty Moves Like</p>
  <svg class="arrow" style="left:80px" width="16" height="26" viewBox="0 0 16 26"><path d="M14 2L3 13l11 11" stroke="#fff" stroke-width="4" fill="none"/></svg>
  <svg class="arrow" style="left:1074px" width="16" height="26" viewBox="0 0 16 26"><path d="M2 2l11 11L2 24" stroke="#fff" stroke-width="4" fill="none"/></svg>

  <div class="service-card" style="left:159px">
    <div class="photo" role="img" aria-label="Movers unloading an exhibit from an orange box truck" style="background:linear-gradient(160deg,#c9d2d8,#e07a2a 45%,#8a8f88)"></div>
    <h3>Exhibits</h3>
    <p>Lorem ipsum dolor sit amet, conse<br>ctetuer adipiscing</p>
    <a class="btn">Read More »</a>
  </div>
  <div class="service-card" style="left:461px">
    <div class="photo" role="img" aria-label="Truck carrying a large display screen in front of city buildings" style="background:linear-gradient(160deg,#e8eef2,#b8c2c8 50%,#6e7478)"></div>
    <h3>Displays</h3>
    <p>Lorem ipsum dolor sit amet, conse<br>ctetuer adipiscing</p>
    <a class="btn">Read More »</a>
  </div>
  <div class="service-card" style="left:763px">
    <div class="photo" role="img" aria-label="Crane truck lifting manufacturing equipment" style="background:linear-gradient(160deg,#dde3e6,#c9b14a 40%,#7a7f80)"></div>
    <h3>Manufacturing Equipment</h3>
    <p>Lorem ipsum dolor sit amet, conse<br>ctetuer adipiscing</p>
    <a class="btn">Read More »</a>
  </div>
</section>

<section class="why">
  <h2 class="section-title slab" style="top:70px">WHY <em>CHOOSE US</em></h2>
  <svg class="divider" style="top:106px" viewBox="0 0 120 14"><line x1="0" y1="7" x2="50" y2="7" stroke="#aaa"/><line x1="70" y1="7" x2="120" y2="7" stroke="#aaa"/><rect x="55" y="2" width="10" height="10" rx="2" fill="none" stroke="#888" stroke-width="1.5"/></svg>

  <div class="why-box" style="left:161px;background:var(--box1)">
    <svg width="84" height="40" viewBox="0 0 84 40"><rect x="2" y="6" width="52" height="24" fill="none" stroke="#fff" stroke-width="3"/><path d="M56 14h14l10 9v7H56z" fill="#fff"/><circle cx="16" cy="34" r="5" fill="#fff"/><circle cx="40" cy="34" r="5" fill="#fff"/><circle cx="70" cy="34" r="5" fill="#fff"/></svg>
    <h3>Quality Transportation</h3>
    <p>Lorem ipsum dolor sit amet, conse ctetuer adipiscing ipsum dolor sit amet, conse ctetuer</p>
    <span class="plus">+</span>
  </div>
  <div class="why-box" style="left:454px;background:var(--box2)">
    <svg width="56" height="60" viewBox="0 0 56 60"><circle cx="28" cy="20" r="14" fill="#fff"/><path d="M12 20a16 16 0 0132 0" stroke="#fff" stroke-width="3" fill="none"/><path d="M4 60c0-14 10-22 24-22s24 8 24 22z" fill="#fff"/></svg>
    <h3>Customer Service</h3>
    <p>Lorem ipsum dolor sit amet, conse ctetuer adipiscing ipsum dolor sit amet, conse ctetuer</p>
    <span class="plus">+</span>
  </div>
  <div class="why-box" style="left:747px;background:var(--box3)">
    <svg width="54" height="54" viewBox="0 0 54 54"><g fill="none" stroke="#fff" stroke-width="4"><circle cx="20" cy="32" r="10"/><circle cx="40" cy="14" r="7"/></g><g stroke="#fff" stroke-width="5"><path d="M20 16v6M20 42v6M4 32h6M30 32h6M9 21l4 4M27 39l4 4M9 43l4-4M27 25l4-4"/><path d="M40 3v4M40 21v4M29 14h4M47 14h4" stroke-width="4"/></g></svg>
    <h3>Technology In Our Business</h3>
    <p>Lorem ipsum dolor sit amet, conse ctetuer adipiscing ipsum dolor sit amet, conse ctetuer</p>
    <span class="plus">+</span>
  </div>
</section>

<section class="blog on-dark">
  <h2 class="section-title slab" style="top:80px">LATEST BLOG</h2>
  <svg class="divider" style="top:115px" viewBox="0 0 120 14"><line x1="0" y1="7" x2="50" y2="7" stroke="#777"/><line x1="70" y1="7" x2="120" y2="7" stroke="#777"/><rect x="55" y="2" width="10" height="10" rx="2" fill="none" stroke="#bbb" stroke-width="1.5"/></svg>

  <article class="post" style="left:163px">
    <div class="photo" role="img" aria-label="Rows of colourful trucks parked in a large yard" style="background:linear-gradient(160deg,#c8ccd0,#b3583a 50%,#6b6f72)"></div>
    <div class="date">12 <span>SEP</span><b>2016</b></div>
    <div class="meta"><span>&#9679; Dara Quill</span><span>&#9632; 111</span></div>
    <h3>Lorem ipsum dolor sit amet...</h3>
    <p>consectetuer adipiscing elit, sed diam nonummy nibh euismod tincidunt ut laoreet</p>
    <a class="btn">Read More »</a>
  </article>
  <article class="post" style="left:470px">
    <div class="photo" role="img" aria-label="White semi truck and trailer parked on a lot" style="background:linear-gradient(160deg,#d8e2ea,#e8ecee 45%,#7f8a7c)"></div>
    <div class="date">12 <span>SEP</span><b>2016</b></div>
    <div class="meta"><span>&#9679; Dara Quill</span><span>&#9632; 111</span></div>
    <h3>Lorem ipsum dolor sit amet...</h3>
    <p>consectetuer adipiscing elit, sed diam nonummy nibh euismod tincidunt ut laoreet</p>
    <a class="btn">Read More »</a>
  </article>
  <article class="post" style="left:777px">
    <div class="photo" role="img" aria-label="Hand using an in-cab tracking device" style="background:linear-gradient(160deg,#2a2c2e,#55595c 50%,#c9a88a)"></div>
    <div class="date">12 <span>SEP</span><b>2016</b></div>
    <div class="meta"><span>&#9679; Dara Quill</span><span>&#9632; 111</span></div>
    <h3>Lorem ipsum dolor sit amet...</h3>
    <p>consectetuer adipiscing elit, sed diam nonummy nibh euismod tincidunt ut laoreet</p>
    <a class="btn">Read More »</a>
  </article>
</section>

<section class="newsletter">
  <svg class="abs" style="left:160px;top:18px" width="36" height="36" viewBox="0 0 36 36"><circle cx="18" cy="18" r="18" fill="#f26a10"/><rect x="9" y="12" width="18" height="13" rx="1" fill="#fff"/><path d="M9 13l9 6 9-6" stroke="#f26a10" stroke-width="1.5" fill="none"/></svg>
  <div class="title">Newsletter Signup</div>
  <svg class="abs" style="left:462px;top:16px" width="24" height="42" viewBox="0 0 24 42"><path d="M3 2l18 19L3 40" stroke="#f26a10" stroke-width="2.5" fill="none"/></svg>
  <input type="text" value="Your e-mail" aria-label="Your e-mail">
  <a class="btn">SIGN UP</a>
</section>

<footer class="site-footer">
  <h4 style="left:163px;width:140px">Quick Links</h4>
  <ul class="links"><li>Home</li><li>About Us</li><li>Careers</li><li>Services</li><li>Blog</li><li>Contact Us</li></ul>

  <h4 style="left:369px;width:180px">Contact Detail</h4>
  <div class="contact-detail">
    <strong style="color:#fff">Velmora</strong><br>Lorem ipsum dolor sit amet, sed<br>diam nonummy nibh.
    <div class="row"><span style="color:var(--orange)">&#9742;</span>555-014-2870</div>
    <div class="row"><span style="color:var(--orange)">&#9113;</span>555-014-2870</div>
    <div class="row"><span style="color:var(--orange)">&#9993;</span>info@velmora.com</div>
  </div>

  <h4 style="left:598px;width:180px">Quick Inquiry</h4>
  <div class="inquiry">
    <div>Name</div><div>Email</div><div>Message</div>
    <a class="btn">Submit</a>
  </div>

  <div class="footer-brand"><span class="mark"></span>VELMORA</div>
  <div class="social-foot"><span></span><span></span><span></span><span></span><span></span></div>
</footer>

<div class="copyright">Copyright © 2016 <em>VELMORA</em>. All Right Reserved.</div>

</body>
</html>
```